A golden web-design opportunity

I have created a quick website (www.brintavexgroup.com.au) but I would like to have the website “polished” to look more professional and have a better consistency.

I would like the website to come across as a genuine, professional insight into our business culture but unfortunately my creative skills have reached their limit.

I have attached a media kit PDF so you are better able to establish what are about.
Updates

Hello All! I just wanted to let everyone know that I do not require an ecommerce site! My website is for potential clients to visit, see what we do and get my contact details...

Gathering more feedback

Hello All, I just wanted to let contestants know that there is not a requirement for my team to be mentioned on the website. I cover in person this as part of my presentation with clients. I have uploaded a new Presentation PDF that has this information excluded. Have a good day!

Target Market(s)

Telecommunications professionals; service delivery partners; white collar executives; construction

Industry/Entity Type

Data Communication

Coding

Coded - Design and coding required

Number of Pages Required

3 page

Font styles to use
Other font styles liked:
• Designers discretion

Colors

Designer to choose colors to be used in the design.

Requirements
Must have
• Must be designed so that I can upload it to Plesk, I think that wordpress is preferred.
• - Page:
• - 1 - Full page is a requirement i.e. the website makes full use of the whole screen
• - 2 - Colour scheme must be "muted" and not agressive
• - Links:
• - 1 - All links will work e.g. "E-Mail us" should work
• - 2 - The page identifier ("[LOGO] Home | Brintavex Gruop) will show the Brintavex logo
• - 3 - A link to facebook and linkedin
• - https://www.facebook.com/brintavexgroup
• - https://www.linkedin.com/company/brintavex-group-pty-ltd/
• - 4 - The phone number icon can be clicked on to make a call
• - 5 - The E-Mail icon can be clicked on to send an E-Mail
Nice to have
• Font:
• - 1 - Rounded is preferred
• - 2 - Colour with reference the logo colours (if possible)
Should not have
• Colour:
• - 1 - To much contrast between colours i.e. balck background with white writing
• - 2 - aggressive colour schemes
• - 3 - Names of Brintavex consultants... These guys are also used by my competetion, only martin is required

```html
<!DOCTYPE html>
<html lang="en">
<head>
<meta charset="utf-8">
<title>Home | Brintavex Gruop</title>
<link href="https://fonts.googleapis.com/css2?family=Poppins:wght@300;400;500;600&family=Oswald:wght@500&display=swap" rel="stylesheet">
<style>
:root{
  --blue:#1f9cd6;
  --blue-dark:#1784b8;
  --blue-soft:#e4f4fb;
  --blue-pale:#cfeaf6;
  --ink:#2c3440;
  --text:#5d6670;
  --line:#d6dde2;
  --foot:#2f3338;
  --white:#ffffff;
}
*{margin:0;padding:0;box-sizing:border-box}
html,body{width:1200px;height:5056px;overflow:hidden}
body{font-family:'Poppins',sans-serif;color:var(--text);background:var(--white);position:relative;font-size:14px;line-height:1.6}
.abs{position:absolute}
.ph{position:absolute}
a{color:inherit;text-decoration:none}

/* header */
.site-header{position:absolute;top:0;left:0;width:1200px;height:100px;background:var(--white)}
.brand{position:absolute;left:88px;top:30px;display:flex;align-items:center;gap:10px;font-weight:600;font-size:22px;color:var(--blue-dark)}
.brand-dot{width:34px;height:34px;border-radius:50%;background:var(--blue)}
.main-nav{position:absolute;right:80px;top:22px;display:flex;gap:14px;font-size:15px;color:var(--ink)}
.main-nav a{padding:8px 22px}
.main-nav a.is-current{border:1px solid var(--line);box-shadow:0 2px 6px rgba(0,0,0,.08)}

/* hero */
.hero{position:absolute;top:100px;left:0;width:1200px;height:475px;background:linear-gradient(135deg,#3d7e9c,#5fa2c0 55%,#3f7f9e)}
.hero-title{position:absolute;top:120px;width:100%;text-align:center;font-family:'Oswald',sans-serif;font-weight:500;font-size:66px;letter-spacing:4px;color:var(--white)}
.hero-sub{position:absolute;top:212px;width:100%;text-align:center;font-weight:600;font-size:24px;letter-spacing:3px;color:var(--white)}
.hero-btn{position:absolute;top:270px;left:523px;width:154px;height:40px;border:2px solid var(--white);color:var(--white);font-size:15px;text-align:center;line-height:36px}

/* value cards */
.value-card{position:absolute;top:660px;width:340px;height:245px;background:var(--blue-soft);text-align:center;padding:26px 26px}
.value-card.is-featured{top:648px;height:270px;background:var(--blue);color:var(--white);padding-top:38px;box-shadow:0 6px 16px rgba(0,0,0,.15)}
.value-card h3{font-size:19px;font-weight:500;color:var(--ink);margin:12px 0 6px}
.value-card.is-featured h3{color:var(--white)}
.value-card p{font-size:12px;line-height:1.7}
.value-card .more{display:block;margin-top:14px;font-size:12px;color:var(--blue-dark)}
.value-card.is-featured .more{color:var(--white)}

h2.section-title{font-size:30px;font-weight:500;color:var(--ink);line-height:1.2}
.btn{display:inline-block;background:var(--blue);color:var(--white);font-size:14px;padding:8px 22px}

/* story */
.story-text{left:88px;top:1030px;width:560px;font-size:14.5px;line-height:1.85}
.story-text p{margin-bottom:24px}

/* services */
.service-list{list-style:none;margin-top:26px}
.service-list li{display:flex;align-items:center;gap:16px;height:37px;font-size:14px;color:var(--ink)}
.service-list svg{flex:none}

/* innovation */
.feature h4{font-size:16px;font-weight:600;color:var(--ink);margin:16px 0 6px}
.feature p{font-size:12.5px;line-height:1.75}

/* testimonials */
.testimonials{position:absolute;top:2965px;left:0;width:1200px;height:405px;background:var(--blue);color:var(--white);text-align:center}
.testimonials h2{font-size:28px;font-weight:500;line-height:1.35;padding-top:30px}
.testimonials .lead{font-size:13px;margin-top:10px}
.quote{position:absolute;top:165px;width:495px;height:205px;background:var(--blue-dark);text-align:left;padding:22px 26px;font-size:12.5px;line-height:1.7}
.quote cite{display:block;margin-top:10px;font-style:normal;font-size:12px;opacity:.9}

/* field reporting */
.field-title{left:88px;top:3455px}
.field-title .big{font-size:42px;font-weight:500;color:var(--blue);line-height:1.15}
.field-title .mid{font-size:32px;color:#5bb6e0;line-height:1.2}
.field-title .tag{font-size:30px;font-weight:300;color:var(--text);line-height:1.25;margin-top:14px;width:470px}
.field-title .tag em{font-style:normal;color:var(--blue)}
.info-box{position:absolute;left:88px;width:460px;background:var(--blue-soft);color:var(--blue-dark);font-size:12.5px;padding:14px 18px;line-height:1.7}
.partner{left:88px;top:3900px;display:flex;align-items:center;gap:10px;font-size:22px;font-weight:600;color:var(--blue-dark)}

/* completion */
.step{position:absolute;left:525px;display:flex;gap:20px;width:590px}
.step .num{flex:none;width:60px;height:60px;background:var(--blue);color:var(--white);font-size:22px;font-weight:500;display:flex;align-items:center;justify-content:center}
.step h4{font-size:15px;font-weight:600;color:var(--ink)}
.step p{font-size:12.5px;line-height:1.7}

/* contact */
.contact-head{top:4470px;width:1200px;text-align:center}
.contact-head h2{font-size:36px;font-weight:500;color:var(--blue);line-height:1.2}
.contact-head .sub{font-size:18px;color:var(--ink)}
.contact-head .intro{font-size:15px;margin-top:14px}
.field{position:absolute;border-bottom:1px solid var(--line);font-size:13px;color:#98a1a8;padding-bottom:8px}

/* footer */
.site-footer{position:absolute;top:5005px;left:0;width:1200px;height:51px;background:var(--foot);color:#b9c0c6;font-size:11.5px}
.site-footer .legal{position:absolute;left:88px;top:16px}
.site-footer .social{position:absolute;right:88px;top:17px;display:flex;gap:14px}
.site-footer .social a{width:16px;height:16px;border-radius:50%;background:#b9c0c6}
</style>
</head>
<body>

<header class="site-header">
  <a class="brand" href="https://www.brintavexgroup.com.au"><span class="brand-dot"></span>Brintavex</a>
  <nav class="main-nav">
    <a class="is-current" href="#">Home</a><a href="#">Our Story</a><a href="#">Products</a><a href="#">Our Projects</a><a href="#">Services</a><a href="#">Contacts</a>
  </nav>
</header>

<section class="hero" role="img" aria-label="Blue-tinted photo of hands typing on a laptop keyboard">
  <h1 class="hero-title">PROJECT DELIVERY</h1>
  <div class="hero-sub">DONE DIFFERENTLY</div>
  <a class="hero-btn" href="#">Find out more</a>
</section>

<article class="value-card" style="left:90px">
  <svg width="52" height="52" viewBox="0 0 52 52" fill="none" stroke="#1784b8" stroke-width="2"><circle cx="26" cy="22" r="11"/><path d="M21 36h10M22 41h8M26 4v5M8 22h5M39 22h5"/></svg>
  <h3>Innovation</h3>
  <p>We have developed apps that allow our clients access to construction data at the click of a button.</p>
  <a class="more" href="#">Read More &gt;</a>
</article>
<article class="value-card is-featured" style="left:430px">
  <svg width="52" height="52" viewBox="0 0 52 52" fill="none" stroke="#fff" stroke-width="2"><circle cx="26" cy="26" r="6"/><circle cx="26" cy="8" r="4"/><circle cx="26" cy="44" r="4"/><circle cx="9" cy="17" r="4"/><circle cx="43" cy="17" r="4"/><circle cx="9" cy="35" r="4"/><circle cx="43" cy="35" r="4"/></svg>
  <h3>Collaboration</h3>
  <p>We view ourselves as an extension of our client. We believe effective collaboration is intrinsically linked to both of our successes.</p>
  <a class="more" href="#">Read More &gt;</a>
</article>
<article class="value-card" style="left:775px">
  <svg width="52" height="52" viewBox="0 0 52 52" fill="none" stroke="#1784b8" stroke-width="2"><path d="M26 5l18 10v22L26 47 8 37V15z"/><path d="M8 15l18 10 18-10M26 25v22"/></svg>
  <h3>Integrity</h3>
  <p>We believe having a culture that strongly promotes integrity is the key to ensuring longevity in the telecommunications industry.</p>
  <a class="more" href="#">Read More &gt;</a>
</article>

<h2 class="section-title abs" style="left:88px;top:970px">Our Story</h2>
<div class="story-text abs">
  <p>We are an innovative telecommunications services company. We believe technology can truly change peoples' lives, so we are working with Victoria's most respected delivery partners to complete unique projects state-wide.</p>
  <p>We are focusing on three key areas that we hope will build our distinct brand within the Australian telecommunications industry.</p>
</div>
<a class="btn abs" style="left:88px;top:1210px" href="#">Read More</a>
<div class="ph" style="left:700px;top:968px;width:465px;height:280px;background:linear-gradient(135deg,#6e8a76,#c9d2c4 50%,#7a8f9a)" role="img" aria-label="Photo of a technician testing a fibre cable with a handheld meter"></div>

<div class="ph" style="left:0;top:1308px;width:590px;height:547px;background:linear-gradient(135deg,#3b4a66,#8a9bb5 50%,#2d3a50)" role="img" aria-label="Photo of a network test instrument connected to patch cables"></div>
<h2 class="section-title abs" style="left:612px;top:1305px">Our Services</h2>
<div class="abs" style="left:612px;top:1362px;width:505px">
  <p style="font-size:12.5px;line-height:1.75">Working with Brintavex Gruop enables a single point of contact for your entire project. We have a wide range of specialties and in-house capabilities that allow us to take on full responsibility for projects. Working with Brintavex reduces clients' deployment costs and time to complete the project.</p>
  <ul class="service-list">
    <li><svg width="26" height="22"><circle cx="13" cy="11" r="8" fill="none" stroke="#1f9cd6" stroke-width="2"/></svg>Project Management (Certified ProjectCert practitioner)</li>
    <li><svg width="26" height="22"><rect x="5" y="4" width="16" height="14" fill="none" stroke="#1f9cd6" stroke-width="2"/></svg>Asbestos removal</li>
    <li><svg width="26" height="22"><path d="M3 15h20M7 8h12" stroke="#1f9cd6" stroke-width="2"/></svg>Pit and pipe installation</li>
    <li><svg width="26" height="22"><path d="M3 11c5-8 15 8 20 0" fill="none" stroke="#1f9cd6" stroke-width="2"/></svg>Cable hauling (Copper &amp; Fibre)</li>
    <li><svg width="26" height="22"><path d="M3 11h20M13 3v16" stroke="#1f9cd6" stroke-width="2"/></svg>Fibre splicing</li>
    <li><svg width="26" height="22"><circle cx="8" cy="11" r="4" fill="#1f9cd6"/><circle cx="18" cy="11" r="4" fill="none" stroke="#1f9cd6" stroke-width="2"/></svg>Copper jointing</li>
    <li><svg width="26" height="22"><rect x="4" y="5" width="18" height="12" rx="2" fill="none" stroke="#1f9cd6" stroke-width="2"/></svg>Fibre integration</li>
    <li><svg width="26" height="22"><path d="M5 17l8-12 8 12z" fill="none" stroke="#1f9cd6" stroke-width="2"/></svg>Recoverable works</li>
    <li><svg width="26" height="22"><path d="M13 20V6M6 8c4-5 10-5 14 0" fill="none" stroke="#1f9cd6" stroke-width="2"/></svg>Telecommunication rigging</li>
  </ul>
</div>

<div class="abs" style="left:88px;top:1908px">
  <h2 class="section-title" style="color:var(--blue)">Innovation.</h2>
  <h2 class="section-title">Creating easy to manage processes.</h2>
</div>
<div class="feature abs" style="left:88px;top:2025px;width:410px">
  <div style="height:265px;background:linear-gradient(135deg,#c5cdd4,#f2f3f4 50%,#9aa7b1)" role="img" aria-label="Photo of colleagues reviewing documents at a desk"></div>
  <h4>Tailored Onboarding</h4>
  <p>When we onboard all employees and contractors we ensure they have all of the industry standard certificates. Using the StaffTrack system allows us to easily tailor our onboarding process to match the needs of our clients and because everything is done online these records can be shared at the click of a button.</p>
</div>
<div class="feature abs" style="left:612px;top:2025px;width:503px">
  <div style="height:265px;background:linear-gradient(135deg,#1d2a3a,#4c6a8a 50%,#1b2533)" role="img" aria-label="Photo of server racks in a data room"></div>
  <h4>In-Field data capturing</h4>
  <p>Our field crews are supplied with pre-loaded tablets that have every app they need. The apps give them 24/7 access to our online server (CloudVault) allowing them to upload documentation or photos at any time. Making accessibility convenient has removed one of field based works' biggest obstacles: getting paperwork back to the office unscathed.</p>
</div>
<div class="feature abs" style="left:88px;top:2485px;width:410px">
  <div style="height:265px;background:linear-gradient(135deg,#1e3554,#6d8fb5 50%,#22395a)" role="img" aria-label="Photo of a compass needle pointing to the word quality"></div>
  <h4>Quality management</h4>
  <p>Brintavex Gruop has a Quality Management Plan. As part of our QMP we are unique in the fact that we complete samples of quality control &amp; inspections of installation; we ensure quality after care and we also quality control completion documents ensuring your experience is simple and problem free.</p>
</div>
<div class="feature abs" style="left:612px;top:2485px;width:503px">
  <div style="height:265px;background:linear-gradient(135deg,#b9b9b5,#ededea 50%,#a8a8a4)" role="img" aria-label="Photo of a pen resting on a printed job form"></div>
  <h4>Completion documentation overhaul</h4>
  <p>Our field crews are supplied with pre-loaded tablets that have every app they need. The apps give them 24/7 access to our online server (CloudVault) allowing them to upload documentation or photos at any time. Making accessibility convenient has removed one of field based works' biggest obstacles: getting paperwork back to the office unscathed.</p>
</div>

<section class="testimonials">
  <h2>We believe in providing the best service to our clients,<br>past, present and future</h2>
  <p class="lead">Here are some accolades our project manager, Martin Holloway has received from stakeholders involved<br>with major projects he has worked on in the past.</p>
  <blockquote class="quote" style="left:88px">&ldquo;In my role as Team Leader of technical services at the Loddon Vale Shire I have worked with Martin and his project team completing the reinstated works at a local pound site. The team was very easy to deal with and their field crews complete their work to a very high standard. I would like to thank Martin and his team for their efforts within the shire.&rdquo;<cite>&mdash;Daniel Ferro, Northbank Water, 2018</cite></blockquote>
  <blockquote class="quote" style="left:618px">&ldquo;As well as the clients endorsement, the quality of Martin's team's work on the recoverable works project was also acknowledged by the SCRA, who were blown away by the speed and quality of the copper cutovers.&rdquo;<cite>&mdash;Riverline Rail Works, 2017</cite></blockquote>
</section>

<div class="field-title abs">
  <div class="big">Field reporting.</div>
  <div class="mid">Made simple.</div>
  <div class="tag">We've been tirelessly to create an <em>easy to use</em> reporting system.</div>
</div>
<div class="info-box" style="top:3690px">We have worked with FormLoop to create simple forms that capture field data in an easy to use app. Reports are easy to obtain and can be downloaded in many popular formats.</div>
<div class="info-box" style="top:3802px">Completed forms are sent from the app to our online server for storage. No need for satchels or scanning, simplifying reporting.</div>
<div class="partner abs"><span class="brand-dot" style="width:40px;height:40px"></span>FormLoop</div>
<div class="ph" style="left:612px;top:3430px;width:588px;height:560px;background:linear-gradient(135deg,#1f2326,#5a6066 50%,#2a2e31)" role="img" aria-label="Two mobile phones showing field reporting form screens"></div>

<div class="ph" style="left:0;top:4065px;width:500px;height:365px;background:var(--blue-pale)"></div>
<div class="ph" style="left:30px;top:4090px;width:420px;height:255px;background:linear-gradient(135deg,#2b2f33,#d7dde1 50%,#3a3f44)" role="img" aria-label="Laptop showing a cloud folder of completion files"></div>
<div class="abs" style="left:525px;top:4058px">
  <h2 class="section-title" style="font-size:32px">Practical Completion.</h2>
  <h2 class="section-title" style="font-size:32px;color:var(--blue)">Made easy.</h2>
</div>
<p class="abs" style="left:525px;top:4150px;width:590px;font-size:15px;line-height:1.7">Our clients are our priority. That's why we have created an effective completions system that can be utilised 24/7.</p>
<div class="step" style="top:4232px"><div class="num">01</div><div><h4>Practical Completion made easy</h4><p>Field documentation is stored in an easy to follow filing system making practical completion easy. A few clicks and you are all done!</p></div></div>
<div class="step" style="top:4330px"><div class="num">02</div><div><h4>Online storage</h4><p>Our completion files are available 24/7 on a secure cloud storage platform (CloudVault) via links provided to our clients.</p></div></div>

<div class="contact-head abs">
  <h2>Connecting with</h2>
  <div class="sub">Brintavex Gruop</div>
  <p class="intro">Brintavex Gruop understands business and we take pride in helping Victorian businesses meet their goals.</p>
</div>
<div class="ph" style="left:88px;top:4620px;width:420px;height:370px;background:linear-gradient(160deg,#9fb0bd,#c4cfd7 60%,#2f8ec2)" role="img" aria-label="Map of Australia with Victoria highlighted in blue"></div>
<div class="abs" style="left:612px;top:4612px;font-size:13px;line-height:1.7;color:var(--ink)">
  Let Brintavex Gruop be part of your business's journey,<br>click an icon below to get in touch online
  <div style="margin-top:10px;font-size:16px;color:var(--blue)"><a href="tel:+61400555218">call Martin</a></div>
  <div style="font-size:16px">on <a href="tel:+61400555218">+61 400 555 218</a></div>
</div>
<div class="field" style="left:612px;top:4748px;width:240px">&#9679;&nbsp; Name</div>
<div class="field" style="left:875px;top:4748px;width:240px">&#9679;&nbsp; Email</div>
<div class="field" style="left:612px;top:4825px;width:503px;height:70px">&#9679;&nbsp; Message</div>
<a class="btn abs" style="left:985px;top:4930px" href="mailto:info@brintavexgroup.com.au">Send Message</a>

<footer class="site-footer">
  <div class="legal">&copy; 2018 All Rights Reserved. Terms of Use and Privacy Policy</div>
  <div class="social">
    <a href="https://www.facebook.com/brintavexgroup" aria-label="Facebook"></a>
    <a href="https://www.linkedin.com/company/brintavex-group-pty-ltd/" aria-label="LinkedIn"></a>
  </div>
</footer>

</body>
</html>
```